Hemp Infused Health Care Products Needs New Labels

Need a label design I can utilize for different products I create, lotion, muscle balm, lip balm, etc. Currently I have a Lumo Vale Soothing Cream label that I created that is rectangle and I want to improve it; more marketable and professional. Create a Circular label also with the words around the circle not straight across This one will be Lumo Vale Muscle Balm. Rec Label is w 5" h 2.5" Circle Label Diameter 2.8"
Target Market(s)
MMJ Dispensaries and online sales. Medical Patients.
Industry/Entity Type
Health And Wellness
Requirements
Must have
- The logo design
- Lumo Vale Soothing Cream
- Lumo Vale Muscle Balm on the round label
Nice to have
- You add some flare to mine to make it more professional and marketable. This will end up being my brand.
Should not have
- No reference or photos of cannabis

```html
<!DOCTYPE html>
<html lang="en">
<head>
<meta charset="utf-8">
<title>Lumo Vale Muscle Balm – Round Label</title>
<link rel="stylesheet" href="https://fonts.googleapis.com/css2?family=Cinzel:wght@700&family=Raleway:wght@500;800&display=swap">
<style>
  :root {
    --navy: #2e3192;
    --green: #7cc242;
    --peach: #f6c48f;
    --cream: #e9efe0;
    --aqua-light: #dcf1ef;
    --aqua: #a8d8d5;
    --sky: #2a9fd8;
    --ink: #4a4a4a;
    --white: #ffffff;
    --page: #fdf9f9;
  }
  html, body {
    margin: 0;
    width: 1200px;
    height: 677px;
    overflow: hidden;
    background: var(--page);
  }
  .canvas { display: block; width: 1200px; height: 677px; }
  .rim { fill: var(--navy); }
  .info-band { fill: url(#bandGradient); }
  .green-ring { fill: var(--green); }
  .title-band { fill: var(--navy); }
  .center-disc { fill: url(#discGradient); }
  .brand-dot { fill: var(--sky); }
  .info-text {
    font-family: "Raleway", sans-serif;
    font-weight: 500;
    fill: var(--ink);
  }
  .info-text .info-label { font-weight: 800; fill: var(--navy); }
  .ingredients { font-size: 17.5px; letter-spacing: 0.2px; }
  .directions { font-size: 19px; }
  .product-title {
    font-family: "Cinzel", serif;
    font-weight: 700;
    font-size: 30px;
    letter-spacing: 1px;
    fill: var(--white);
  }
  .claim {
    font-family: "Cinzel", serif;
    font-weight: 700;
    fill: var(--white);
  }
  .claim-top { font-size: 14px; }
  .claim-bottom { font-size: 15px; }
  .brand-name {
    font-family: "Cinzel", serif;
    font-weight: 700;
    font-size: 22px;
    letter-spacing: 1px;
    fill: var(--navy);
  }
</style>
</head>
<body>
<svg class="canvas" viewBox="0 0 1200 677" xmlns="http://www.w3.org/2000/svg">
  <defs>
    <radialGradient id="bandGradient" cx="0.5" cy="0.5" r="0.5">
      <stop offset="0.72" stop-color="var(--cream)"/>
      <stop offset="1" stop-color="var(--peach)"/>
    </radialGradient>
    <radialGradient id="discGradient" cx="0.5" cy="0.45" r="0.55">
      <stop offset="0" stop-color="var(--aqua-light)"/>
      <stop offset="1" stop-color="var(--aqua)"/>
    </radialGradient>
    <path id="ingredientsArc" d="M482,542.4 A236,236 0 1,1 718,133.6 A236,236 0 1,1 482,542.4"/>
    <path id="directionsArc" d="M397.2,283.6 A210,210 0 1,1 772,458.5"/>
    <path id="titleArc" d="M464.1,401.4 A150,150 0 1,1 735.9,401.4"/>
    <path id="claimBottomArc" d="M438.3,396.8 A172,172 0 0,0 761.7,396.8"/>
    <path id="claimTopArc" d="M538.2,470.3 A146,146 0 0,0 661.8,470.3"/>
  </defs>

  <g class="round-label">
    <circle class="rim" cx="600" cy="338" r="268"/>
    <circle class="info-band" cx="600" cy="338" r="260"/>
    <circle class="green-ring" cx="600" cy="338" r="198"/>
    <circle class="title-band" cx="600" cy="338" r="191"/>
    <circle class="green-ring" cx="600" cy="338" r="133"/>
    <circle class="center-disc" cx="600" cy="338" r="128"/>

    <text class="info-text ingredients">
      <textPath href="#ingredientsArc" startOffset="1%"><tspan class="info-label">ACTIVE INGREDIENT:</tspan> Hemp Infused Organic Coconut Oil<tspan class="info-label" dx="34">ESSENTIAL OILS:</tspan> Peppermint, lavender, Frankincense, Wild Orange, Ginger, Rosemary</textPath>
    </text>

    <text class="info-text directions" text-anchor="middle">
      <textPath href="#directionsArc" startOffset="50%"><tspan class="info-label">TO USE:</tspan> Apply a small Amount to affected area as needed.</textPath>
    </text>

    <text class="product-title" text-anchor="middle">
      <textPath href="#titleArc" startOffset="50%">LUMO VALE MUSCLE BALM</textPath>
    </text>

    <text class="claim claim-top" text-anchor="middle">
      <textPath href="#claimTopArc" startOffset="50%">MADE WITH</textPath>
    </text>
    <text class="claim claim-bottom" text-anchor="middle">
      <textPath href="#claimBottomArc" startOffset="50%">THERAPEUTIC GRADE ESSENTIAL OILS</textPath>
    </text>

    <g class="brand-mark">
      <circle class="brand-dot" cx="600" cy="318" r="34"/>
      <text class="brand-name" x="600" y="398" text-anchor="middle">SOLACE GROVE</text>
    </g>
  </g>
</svg>
</body>
</html>
```